Letterhead Design Project

Initially, we would like to review our letterheads.

Something simple which uses our corporate imagery well and is nicely balanced.

Please note that I will be following up this letter-head with some customised quote templates and similarly customisable collateral in the next few weeks.

Target Market(s)

Enterprise business

Industry/Entity Type

Quote

Requirements
Must have
• The Nexora9 logo
See www.nexora9.com.au

Our tagline "Enterprise Hosting, Messaging and Server Virtualisation"

Our website address

Ideally in our colour pallette, but will consider submissions which look fantastic and necessitate other colours.

```html
<!DOCTYPE html>
<html lang="en">
<head>
<meta charset="utf-8">
<title>Nexora9 Letterhead</title>
<link rel="stylesheet" href="https://fonts.googleapis.com/css2?family=Archivo+Black&family=Questrial&display=swap">
<style>
  :root {
    --brand-red: #d50000;
    --ink: #111111;
    --paper: #ffffff;
  }
  html, body {
    margin: 0;
    padding: 0;
    overflow: hidden;
    background: var(--paper);
  }
  .letterhead {
    position: relative;
    width: 848px;
    height: 1200px;
    background: var(--paper);
    overflow: hidden;
  }
  .masthead {
    position: absolute;
    left: 0;
    top: 0;
    width: 848px;
    height: 110px;
    background: var(--brand-red);
  }
  .brand {
    position: absolute;
    display: flex;
    align-items: center;
    gap: 5px;
  }
  .brand-mark {
    display: block;
    flex: none;
  }
  .brand-name {
    font-family: "Archivo Black", sans-serif;
    color: var(--ink);
    letter-spacing: -1px;
    line-height: 1;
    white-space: nowrap;
  }
  .masthead .brand {
    left: 133px;
    top: 41px;
    width: 150px;
  }
  .masthead .brand-mark {
    width: 30px;
    height: 30px;
    background: var(--paper);
  }
  .masthead .brand-name {
    font-size: 24px;
  }
  .masthead-details {
    position: absolute;
    left: 294px;
    top: 40px;
    width: 419px;
    font-family: "Questrial", sans-serif;
    color: var(--paper);
    font-size: 13.5px;
    letter-spacing: 1.55px;
    line-height: 17px;
  }
  .tagline {
    margin: 0;
    white-space: nowrap;
  }
  .contact-line {
    display: flex;
    justify-content: space-between;
    margin: 0;
    white-space: nowrap;
  }
  .footer-brand {
    left: 345px;
    top: 1116px;
  }
  .footer-brand .brand-mark {
    width: 32px;
    height: 32px;
    background: var(--brand-red);
  }
  .footer-brand .brand-name {
    font-size: 26px;
  }
</style>
</head>
<body>
  <main class="letterhead">
    <header class="masthead">
      <div class="brand">
        <span class="brand-mark"></span>
        <span class="brand-name">Nexora9</span>
      </div>
      <div class="masthead-details">
        <p class="tagline">Enterprise Hosting, Messaging and Server Virtualization</p>
        <p class="contact-line">
          <span class="website">www.nexora9.com.au</span>
          <span class="email">info@nexora9.com.au</span>
        </p>
      </div>
    </header>
    <footer class="brand footer-brand">
      <span class="brand-mark"></span>
      <span class="brand-name">Nexora9</span>
    </footer>
  </main>
</body>
</html>
```